Tarnvik Business Card Design - double sided -plumbing local plumbing company

We have a Plumbing company where the design was create through Pixel Harbour. We would now like a business card designed as well. We want it to be in the colour version of the logo.

Details below for the card.

Phone Number: 0468 215 307
Email: info@tarnvikplumbing.example.au
Website: https://tarnvikplumbing.example.au
We really want a sophisticated design that stand out from the other- informative and timeless.

Target Market(s)

local Canberra market

Industry/Entity Type

Plumbing, gas fitting, hot water

Contact Information for Business Card

Phone number, email, logo and "Supplying all your heating, cooling and hot water needs"

Requirements
Must have
• bust be colourful, must also be though about it being printed on a magnet. must Vik with the logo - I dont want the logo and information chucked onto a white canvas I would prefer it to be smooth and look purposeful

```html
<!DOCTYPE html>
<html lang="en">
<head>
<meta charset="UTF-8">
<title>Tarnvik Business Card</title>
<link rel="stylesheet" href="https://fonts.googleapis.com/css2?family=Poppins:wght@400;600&display=swap">
<style>
  :root {
    --page-bg: #e6e3e3;
    --panel-light: #f3f0f0;
    --brand-blue: #00adef;
    --logo-blue: #1aa6e0;
    --accent-orange: #f7a823;
    --text-white: #ffffff;
  }
  * { margin: 0; padding: 0; box-sizing: border-box; }
  html, body {
    width: 1200px;
    height: 900px;
    overflow: hidden;
    background: var(--page-bg);
    font-family: "Poppins", sans-serif;
  }
  .canvas {
    position: relative;
    width: 1200px;
    height: 900px;
  }
  .business-card {
    position: absolute;
    left: 120px;
    top: 153px;
    width: 960px;
    height: 594px;
    display: flex;
    box-shadow: 0 10px 30px rgba(0, 0, 0, 0.12);
  }
  .card-brand {
    width: 429px;
    background: var(--panel-light);
    display: flex;
    align-items: center;
    justify-content: center;
  }
  .brand-name {
    font-weight: 600;
    font-size: 62px;
    letter-spacing: 1px;
    color: var(--logo-blue);
    text-transform: uppercase;
  }
  .card-divider {
    width: 7px;
    background: var(--accent-orange);
  }
  .card-details {
    flex: 1;
    background: var(--brand-blue);
    color: var(--text-white);
    padding: 124px 0 0 32px;
  }
  .person-name {
    font-weight: 600;
    font-size: 38px;
    line-height: 1.1;
    letter-spacing: 0.5px;
    text-transform: uppercase;
  }
  .person-role {
    font-weight: 400;
    font-size: 27px;
    line-height: 1.2;
  }
  .contact-list {
    list-style: none;
    margin-top: 38px;
  }
  .contact-item {
    display: flex;
    align-items: center;
    gap: 9px;
    font-size: 25.5px;
    line-height: 35px;
  }
  .contact-icon {
    width: 25px;
    height: 25px;
    flex: none;
  }
  .tagline {
    margin-top: 36px;
    font-size: 27px;
    line-height: 35px;
  }
</style>
</head>
<body>
<main class="canvas">
  <section class="business-card">
    <div class="card-brand">
      <span class="brand-name">Tarnvik</span>
    </div>
    <div class="card-divider"></div>
    <div class="card-details">
      <h1 class="person-name">Marcus Ellery</h1>
      <p class="person-role">Managing Director</p>
      <ul class="contact-list">
        <li class="contact-item">
          <svg class="contact-icon" viewBox="0 0 24 24" aria-hidden="true">
            <path d="M6.6 10.8c1.4 2.8 3.8 5.1 6.6 6.6l2.2-2.2c.3-.3.7-.4 1-.2 1.1.4 2.3.6 3.6.6.6 0 1 .4 1 1V20c0 .6-.4 1-1 1C10.6 21 3 13.4 3 4c0-.6.4-1 1-1h3.5c.6 0 1 .4 1 1 0 1.3.2 2.5.6 3.6.1.3 0 .7-.2 1L6.6 10.8z" fill="#fff"/>
          </svg>
          0468 215 307
        </li>
        <li class="contact-item">
          <svg class="contact-icon" viewBox="0 0 24 24" aria-hidden="true">
            <rect x="2" y="5" width="20" height="14" fill="#fff"/>
            <path d="M2 5l10 8 10-8M2 19l7-7M22 19l-7-7" stroke="#00adef" stroke-width="1.6" fill="none"/>
          </svg>
          info@tarnvikplumbing.example.au
        </li>
        <li class="contact-item">
          <svg class="contact-icon" viewBox="0 0 24 24" aria-hidden="true">
            <g fill="none" stroke="#fff" stroke-width="1.6">
              <circle cx="12" cy="12" r="9.5"/>
              <ellipse cx="12" cy="12" rx="4.5" ry="9.5"/>
              <path d="M2.5 12h19M4 7h16M4 17h16"/>
            </g>
          </svg>
          www.tarnvikplumbing.example.au
        </li>
      </ul>
      <p class="tagline">Supplying all your heating<br>cooling and hot water needs</p>
    </div>
  </section>
</main>
</body>
</html>
```